"Recently Leased" flyer for real estate agency

Looking to have a Recently Leased flyer designed. This will be delivered to apartments and houses closely situated to a property we have recently leased. The idea is to get the attention of owner/landlords in the area that may be considering leasing their property in the future and inform them of the great work we are doing locally. I would like the design to be a two sided flyer using the photoshop (PSD) template below (we would like to be able to edit this once complete should we need to update copy etc in the future). I would like the front page to look like our "for lease sign with the leased sticker on it and copy, I dont want it to look like a typical junk mail flyer.

Target Market(s)

Property owners and investors, male and female aged 28-70

Industry/Entity Type

Real Estate

Font styles to use
Sans Serif

Colors

Designer to choose colors to be used in the design.

Requirements
Must have
• Harbor Keystone Logo
• Contact information
• Copy supplied
Nice to have
• Slick, clean design,
Should not have
• too many colours or too busy a design.
• NO PROPERTY PHOTOS ON FRONT - I want this to be generic and not relate to a specific property image which might confuse people.

```html
<!DOCTYPE html>
<html lang="en">
<head>
<meta charset="utf-8">
<title>Harbor Keystone – Recently Leased Flyer</title>
<link rel="stylesheet" href="https://fonts.googleapis.com/css2?family=Lato:wght@300;400;700&display=swap">
<style>
  :root {
    --stage: #d3d4d6;
    --frame: #ffffff;
    --slate: #3f454b;
    --paper: #f2f2f2;
    --teal: #2f7e8e;
    --red: #b0343a;
    --tick: #c8303a;
    --ink: #2e3236;
    --white: #ffffff;
    --hero-top: #0f3d6e;
    --hero-mid: #3d78a8;
    --hero-low: #6fa3c2;
  }
  * { box-sizing: border-box; margin: 0; padding: 0; }
  html, body { width: 1022px; height: 1200px; overflow: hidden; }
  body { background: var(--stage); font-family: "Lato", sans-serif; position: relative; }

  .flyer { position: absolute; top: 185px; width: 383px; height: 830px; background: var(--frame); }
  .flyer--front { left: 95px; }
  .flyer--back { left: 514px; }
  .flyer__sheet { position: absolute; left: 13px; top: 13px; width: 357px; height: 803px; overflow: hidden; }
  .flyer--front .flyer__sheet { background: var(--slate); color: var(--white); }
  .flyer--back .flyer__sheet { background: var(--paper); color: var(--ink); }

  .brand { position: absolute; left: 0; width: 100%; text-align: center; font-weight: 700; font-size: 29px; letter-spacing: 0.5px; color: var(--white); }
  .flyer--front .brand { top: 72px; }
  .flyer--back .brand { top: 64px; }

  .hero { position: absolute; left: 0; top: 0; width: 357px; height: 268px;
    background: linear-gradient(180deg, var(--hero-top) 0%, var(--hero-mid) 55%, var(--hero-low) 100%); }

  .leased { position: absolute; left: 15px; top: 184px; width: 327px; height: 76px; background: var(--red); padding: 6px; }
  .leased__inner { width: 100%; height: 100%; border: 2px solid var(--white); display: flex; align-items: center; justify-content: center;
    font-size: 72px; font-weight: 400; letter-spacing: 1px; line-height: 1; color: var(--white); }

  .copy { position: absolute; left: 27px; width: 303px; font-size: 11.6px; line-height: 14.8px; }
  .copy p { text-align: justify; margin-bottom: 12px; }
  .flyer--front .copy { top: 277px; }
  .flyer--back .copy { top: 296px; }

  .benefits { list-style: none; margin: 14px 0 18px 27px; width: 255px; }
  .benefits li { position: relative; padding-left: 16px; margin-bottom: 6px; text-align: left; }
  .benefits svg { position: absolute; left: 0; top: 3px; width: 9px; height: 9px; }

  .contact { position: absolute; left: 27px; top: 692px; width: 322px; height: 46px; display: flex; align-items: flex-start; }
  .contact__agent { width: 132px; flex: none; }
  .contact__name { font-size: 16.5px; line-height: 20px; }
  .contact__phone { font-size: 16.5px; font-weight: 700; line-height: 20px; display: flex; align-items: center; gap: 2px; white-space: nowrap; }
  .contact__phone svg { width: 13px; height: 13px; flex: none; }
  .contact__divider { width: 14px; height: 48px; margin-top: -2px; flex: none; display: flex; flex-direction: column; align-items: center; }
  .contact__line { width: 1px; flex: 1; background: currentColor; opacity: 0.5; }
  .contact__divider svg { width: 14px; height: 14px; margin: 3px 0; flex: none; }
  .contact__office { padding-left: 14px; font-size: 11px; line-height: 13.5px; }
  .contact__office strong { display: block; font-size: 13.6px; font-weight: 700; line-height: 18px; margin-bottom: 1px; }

  .webband { position: absolute; left: 0; bottom: 0; width: 100%; height: 51px; background: var(--teal); color: var(--white);
    text-align: center; font-size: 14px; line-height: 18.5px; padding-top: 7px; letter-spacing: 0.2px; }
</style>
</head>
<body>

<svg width="0" height="0" style="position:absolute">
  <defs>
    <symbol id="tick" viewBox="0 0 10 10"><circle cx="5" cy="5" r="5" fill="#c8303a"/><path d="M2.6 5.1 4.3 6.7 7.5 3.4" fill="none" stroke="#fff" stroke-width="1.5"/></symbol>
    <symbol id="phone" viewBox="0 0 16 16"><path d="M4 2 6 5 4.8 6.6c.8 1.8 2.4 3.4 4.2 4.2L10.6 9.6l3 2-1.2 2.2C7 13.6 2.4 9 2 3.6Z" fill="none" stroke="currentColor" stroke-width="1.4"/><path d="M9.5 3.5a3 3 0 0 1 3 3M9.5 1.5a5 5 0 0 1 5 5" fill="none" stroke="currentColor" stroke-width="1.2"/></symbol>
    <symbol id="pin" viewBox="0 0 14 14"><path d="M7 1.5a4 4 0 0 0-4 4C3 8.6 7 12.8 7 12.8s4-4.2 4-7.3a4 4 0 0 0-4-4Z" fill="currentColor"/><circle cx="7" cy="5.5" r="1.5" fill="var(--hole)"/></symbol>
  </defs>
</svg>

<section class="flyer flyer--front">
  <div class="flyer__sheet">
    <div class="brand">HARBOR KEYSTONE</div>

    <div class="leased"><div class="leased__inner">LEASED!</div></div>

    <div class="copy">
      <p>We recently leased a property in your building or street. Attracting a great reliable tenant and fantastic return for the owner.</p>
      <p>We received a high number of enquires and applications for this property and have a database of screened and qualified tenants looking to lease in your area.</p>
      <ul class="benefits">
        <li><svg><use href="#tick"/></svg>On average we lease properties 2 weeks faster than the Northern Beaches average</li>
        <li><svg><use href="#tick"/></svg>Strong database of tenants actively looking in the area</li>
        <li><svg><use href="#tick"/></svg>All we do is lease property, no sales – so tenanting and managing your property is our priority</li>
        <li><svg><use href="#tick"/></svg>90 day money back guarantee on our level of service</li>
        <li><svg><use href="#tick"/></svg>Highly competitive, simple all-inclusive pricing.</li>
        <li><svg><use href="#tick"/></svg>Experience the difference of a property management specialist</li>
      </ul>
      <p>Contact <strong>Sam</strong> to get your free rental appraisal or transfer your existing investment to an agency that will give it the attention it deserves and maxamise your return.</p>
    </div>

    <div class="contact">
      <div class="contact__agent">
        <div class="contact__name">Sam Carter</div>
        <div class="contact__phone"><svg><use href="#phone"/></svg>0400 555 218</div>
      </div>
      <div class="contact__divider" style="--hole:#3f454b">
        <span class="contact__line"></span><svg><use href="#pin"/></svg><span class="contact__line"></span>
      </div>
      <div class="contact__office"><strong>Harbor Keystone Agency</strong>Level 1, 18 Marlow Rd,<br>Seacliff NSW 2099</div>
    </div>

    <div class="webband">sam@harborkeystoneagency.com.au<br>www.harborkeystoneagency.com.au</div>
  </div>
</section>

<section class="flyer flyer--back">
  <div class="flyer__sheet">
    <div class="hero" role="img" aria-label="Coastal photo of a surf beach with waves and a headland of houses under a blue sky"></div>
    <div class="brand">HARBOR KEYSTONE</div>

    <div class="copy">
      <p>The fundamental idea behind Harbor Keystone Agency was to give landlords a simple and confidence inspiring experience. We achieve this through:</p>
      <ul class="benefits">
        <li><svg><use href="#tick"/></svg>Unique marketing that goes beyond the standard listing sites and has seen our average days-on-market at 5.9days for 2018.</li>
        <li><svg><use href="#tick"/></svg>A simple, yet competitive fee structure.</li>
        <li><svg><use href="#tick"/></svg>Excellent customer service through an experienced professional property manager.</li>
        <li><svg><use href="#tick"/></svg>Sound advice and communication through out the leasing and management process.</li>
        <li><svg><use href="#tick"/></svg>A simple yet powerful landlord portal which enables owners to view media rich inspection reports, financial reports and maintenance progress at anytime.</li>
        <li><svg><use href="#tick"/></svg>We then back our service promise with a<br>90day money back guarantee.</li>
      </ul>
      <p>If you have been considering leasing your property, purchasing a local investment or aren't happy with your current managing agency, please don't hesitate to contact your local rental specialist for more information:</p>
    </div>

    <div class="contact" style="top:695px">
      <div class="contact__agent">
        <div class="contact__name">Sam Carter</div>
        <div class="contact__phone"><svg><use href="#phone"/></svg>0400 555 218</div>
      </div>
      <div class="contact__divider" style="--hole:#f2f2f2">
        <span class="contact__line"></span><svg><use href="#pin"/></svg><span class="contact__line"></span>
      </div>
      <div class="contact__office"><strong>Harbor Keystone Agency</strong>Level 1, 18 Marlow Rd,<br>Seacliff NSW 2099</div>
    </div>

    <div class="webband">sam@harborkeystoneagency.com.au<br>www.harborkeystoneagency.com.au</div>
  </div>
</section>

</body>
</html>
```